Option Sheet

We need a one page option sheet with a left to right reading of the five options. It should be a one sheet, multiple colors and definitive separations between options This is used in a sales consultation. Backround or colors not in option need to have the follow RGB value (5 red, 20 green, 63 blue)

We added a smaller text file, please change that point

Target Market(s)

Divorce

Industry/Entity Type

Legal

Requirements
Must have
• 1) All five options left to right
• 2)language included in sheet

```html
<!DOCTYPE html>
<html lang="en">
<head>
<meta charset="utf-8">
<title>Five Options Divorce</title>
<link href="https://fonts.googleapis.com/css2?family=Montserrat:wght@400;600;700;800;900&family=Oswald:wght@400;600&display=swap" rel="stylesheet">
<style>
  :root {
    --stage: #d3dffd;
    --sheet: #ffffff;
    --title-blue: #4a7cf7;
    --title-grey: #666666;
    --card: #f1f1f1;
    --text: #5a5a5a;
    --adv: #0b7a4b;
    --dis: #e0141e;
    --rule-grey: #666666;
    --band-blue: #4a7cf7;
    --o1-top: #00874f; --o1-sub: #11cf85;
    --o2-top: #d48a00; --o2-sub: #f9ab18;
    --o3-top: #003d8a; --o3-sub: #0a67d4;
    --o4-top: #0c9eba; --o4-sub: #16cde8;
    --o5-top: #8a3a00; --o5-sub: #c45d12;
  }
  * { box-sizing: border-box; margin: 0; padding: 0; }
  html, body { width: 1200px; height: 1200px; overflow: hidden; }
  body { background: var(--stage); font-family: "Montserrat", sans-serif; position: relative; }

  .sheet {
    position: absolute; left: 0; top: 176px; width: 1200px; height: 847px;
    background: radial-gradient(ellipse at 50% 20%, #ffffff 0%, #f7f7f7 60%, #f3f3f3 100%);
  }
  .title { position: absolute; left: 0; width: 100%; text-align: center; font-weight: 900; line-height: 1; }
  .title-five { top: 46px; font-size: 116px; color: var(--title-blue); letter-spacing: 1px; }
  .title-main { top: 164px; font-size: 96px; color: var(--title-grey); font-weight: 800; letter-spacing: 1px; }

  .option { position: absolute; top: 305px; }
  .tab { position: relative; border-top-right-radius: 10px; overflow: hidden; }
  .tab-number {
    height: 40px; padding-left: 14px; display: flex; align-items: center;
    font-family: "Oswald", sans-serif; font-weight: 600; font-size: 24px; color: #fff; letter-spacing: .3px;
  }
  .tab-name {
    height: 39px; padding-left: 15px; display: flex; align-items: center;
    font-family: "Oswald", sans-serif; font-weight: 400; font-size: 20px; color: #fff;
  }
  .tab-name.dark { color: #1c1c1c; padding-left: 8px; }
  .card {
    background: var(--card); height: 370px; border-top-right-radius: 22px;
    padding: 16px 10px 0 16px;
    box-shadow: 0 5px 4px -2px rgba(0,0,0,.22);
  }
  .label { font-size: 12px; font-weight: 700; letter-spacing: .9px; }
  .label.adv { color: var(--adv); margin-bottom: 6px; }
  .label.dis { color: var(--dis); margin-top: 18px; margin-bottom: 16px; }
  .list { list-style: none; font-size: 13px; line-height: 15.6px; color: var(--text); letter-spacing: .3px; }
  .list li { position: relative; padding-left: 12px; }
  .list.adv li { margin-bottom: 5px; }
  .list.dis li { margin-bottom: 15px; }
  .list li::before {
    content: ""; position: absolute; left: 0; top: 6px; width: 4px; height: 4px; border-radius: 50%;
  }
  .list.adv li::before { background: var(--adv); }
  .list.dis li::before { background: var(--dis); }
  .spaced .list.adv li { margin-bottom: 14px; }
  .spaced .label.dis { margin-top: 10px; margin-bottom: 12px; }

  .o1 { left: 32px; }  .o1 .tab { width: 149px; } .o1 .card { width: 185px; }
  .o2 { left: 232px; } .o2 .tab { width: 182px; } .o2 .card { width: 217px; padding-left: 13px; }
  .o3 { left: 460px; } .o3 .tab { width: 181px; } .o3 .card { width: 216px; }
  .o4 { left: 686px; } .o4 .tab { width: 218px; } .o4 .card { width: 255px; padding-left: 11px; }
  .o5 { left: 951px; } .o5 .tab { width: 181px; } .o5 .card { width: 218px; }

  .o1 .tab-number { background: var(--o1-top); } .o1 .tab-name { background: var(--o1-sub); }
  .o2 .tab-number { background: var(--o2-top); } .o2 .tab-name { background: var(--o2-sub); }
  .o3 .tab-number { background: var(--o3-top); } .o3 .tab-name { background: var(--o3-sub); }
  .o4 .tab-number { background: var(--o4-top); } .o4 .tab-name { background: var(--o4-sub); }
  .o5 .tab-number { background: var(--o5-top); } .o5 .tab-name { background: var(--o5-sub); }

  .rule-grey { position: absolute; left: 0; top: 801px; width: 100%; height: 5px; background: var(--rule-grey); }
  .band-blue { position: absolute; left: 0; top: 811px; width: 100%; height: 36px; background: var(--band-blue); }
</style>
</head>
<body>
<main class="sheet">
  <h1>
    <span class="title title-five">FIVE</span>
    <span class="title title-main">OPTIONS DIVORCE</span>
  </h1>

  <section class="option o1">
    <div class="tab"><div class="tab-number">OPTION #1:</div><div class="tab-name dark">DO NOTHING</div></div>
    <div class="card">
      <h3 class="label adv">ADVANTAGES:</h3>
      <ul class="list adv"><li>Stay married</li><li>No life Changes</li></ul>
      <h3 class="label dis">DISADVANTAGES:</h3>
      <ul class="list dis">
        <li>Remain unhappy,<br>depressed,<br>anxious</li>
        <li>Money and assets<br>may disappear</li>
        <li>What is going<br>to change?</li>
      </ul>
    </div>
  </section>

  <section class="option o2">
    <div class="tab"><div class="tab-number">OPTION #2:</div><div class="tab-name dark">GO TO COUNSELING</div></div>
    <div class="card">
      <h3 class="label adv">ADVANTAGES:</h3>
      <ul class="list adv"><li>Reconcile marriage</li><li>Help make a better life</li></ul>
      <h3 class="label dis">DISADVANTAGES:</h3>
      <ul class="list dis">
        <li>Past issues are<br>highlighted and may<br>drudge up old wounds</li>
        <li>It may just clarify the<br>reasons you need to<br>separate and/or divorce</li>
        <li>Both parties must be<br>invested and willing<br>to participate</li>
      </ul>
    </div>
  </section>

  <section class="option o3">
    <div class="tab"><div class="tab-number">OPTION #3:</div><div class="tab-name">DO IT YOURSELF</div></div>
    <div class="card">
      <h3 class="label adv">ADVANTAGES:</h3>
      <ul class="list adv"><li>No attorney fees</li><li>You are your on attorney</li></ul>
      <h3 class="label dis">DISADVANTAGES:</h3>
      <ul class="list dis">
        <li>People often find that<br>what is “fair,” may in fact,<br>not be truly fair</li>
        <li>Often times, people do<br>not know the risks</li>
        <li>Complicated legal system<br>within intrigue rules</li>
        <li>Unsure how to complete<br>the necessary paperwork<br>and meet the deadlines</li>
      </ul>
    </div>
  </section>

  <section class="option o4">
    <div class="tab"><div class="tab-number">OPTION #4:</div><div class="tab-name dark">LIMITED REPRESENTATION</div></div>
    <div class="card">
      <h3 class="label adv">ADVANTAGES:</h3>
      <ul class="list adv"><li>Balance between going alone<br>and our limited involvement<br>in the case</li></ul>
      <h3 class="label dis">DISADVANTAGES:</h3>
      <ul class="list dis">
        <li>Our terms may not benefit<br>from our legal knowledge</li>
        <li>The legal consequences of<br>your legal documents will not<br>be explained to you so that<br>you can formulate a plan for<br>handling the rest of your case.</li>
        <li>Your spouse or other parties<br>may cause your legal fees to<br>increase significantly without<br>action on your part</li>
      </ul>
    </div>
  </section>

  <section class="option o5 spaced">
    <div class="tab"><div class="tab-number">OPTION #5:</div><div class="tab-name">HIRE US</div></div>
    <div class="card">
      <h3 class="label adv">ADVANTAGES:</h3>
      <ul class="list adv">
        <li>Gain the full benefits of<br>our experience</li>
        <li>Have a team of Family<br>Law focus attorneys</li>
        <li>Often saves you or<br>makes you money<br>in the long run</li>
        <li>Save you time, energy<br>and stress</li>
      </ul>
      <h3 class="label dis">DISADVANTAGES:</h3>
      <ul class="list dis"><li>Initial cost</li></ul>
    </div>
  </section>

  <div class="rule-grey"></div>
  <div class="band-blue"></div>
</main>
</body>
</html>
```